Truck and Trailer lettering for Landscape Company

Looking to continue to brand our landscape business. We recently purchased two new pickup trucks and have two new enclosed trailers on the way. I have attached a picture of the truck(s) (both pickup trucks are identical) and our logo. We have other trucks in our fleet that have our logo on them and have a two tone green stripe running from the hood of the truck to the rear of the truck. The green stripe uses the two green colors of our logo and we wish to have the green stripe on our new trucks and trailers as well. Please keep in mind that we are a very professional company that services high end residential and large commercial clients. We are looking for a professional yet clean and easily identifiable image. Also something that we can use for other trucks, trailers, and equipment that we may purchase in the future.

Industry/Entity Type

Landscape

Requirements
Must have
• Must have the logo, stripe with the two greens from our logo. We would like to see some designs that incorporate the two leaves from our logo into the design elsewhere on the truck and trailer.
Should not have
• No other colors unless they are similar to the ones in our current logo. No changes to our logo, just looking for designs using our current logo

```html
<!DOCTYPE html>
<html lang="en">
<head>
<meta charset="utf-8">
<title>Greenvale Grounds – 24 Foot Trailer Lettering</title>
<link rel="stylesheet" href="https://fonts.googleapis.com/css2?family=Open+Sans:ital,wght@0,700;1,700&family=Alfa+Slab+One&display=swap">
<style>
  :root {
    --green-dark: #2f7238;
    --green-light: #a2c13f;
    --white: #ffffff;
    --frame: #9a9c9e;
    --frame-light: #c9cbcd;
    --hitch: #1b1b1b;
    --tire: #2a2a2a;
    --rim: #d4d6d8;
    --lamp-red: #c8262c;
    --lamp-amber: #e5a21f;
    --shadow: #c4c6c8;
    --title: #222222;
  }
  html, body {
    margin: 0;
    padding: 0;
    width: 1200px;
    height: 845px;
    overflow: hidden;
    background: var(--white);
  }
  .sheet { display: block; width: 1200px; height: 845px; }
  .fill-dark { fill: var(--green-dark); }
  .fill-light { fill: var(--green-light); }
  .fill-white { fill: var(--white); }
  .body-frame { fill: var(--white); stroke: var(--frame); stroke-width: 3; }
  .frame-rail { fill: var(--frame); }
  .hitch { fill: var(--hitch); }
  .tire { fill: var(--tire); }
  .rim { fill: var(--rim); stroke: var(--frame); stroke-width: 2; }
  .ground-shadow { fill: var(--shadow); }
  .lamp-red { fill: var(--lamp-red); }
  .lamp-amber { fill: var(--lamp-amber); }
  .door { fill: none; stroke: var(--frame); stroke-width: 6; }
  .door-handle { fill: var(--hitch); }
  .brand-name {
    font-family: "Open Sans", Arial, sans-serif;
    font-weight: 700;
    fill: var(--green-dark);
  }
  .contact {
    font-family: "Open Sans", Arial, sans-serif;
    font-weight: 700;
    font-style: italic;
  }
  .contact--dark { fill: var(--green-dark); }
  .contact--white { fill: var(--white); }
  .sheet-title {
    font-family: "Alfa Slab One", "Rockwell", serif;
    fill: var(--title);
    letter-spacing: 1px;
  }
</style>
</head>
<body>
<svg class="sheet" viewBox="0 0 1250 880" xmlns="http://www.w3.org/2000/svg">

  <!-- Street side view -->
  <g class="trailer trailer--street-side">
    <rect class="ground-shadow" x="85" y="364" width="800" height="6" rx="3"/>
    <rect class="hitch" x="20" y="286" width="108" height="18" rx="6"/>
    <rect class="hitch" x="50" y="244" width="9" height="56"/>
    <rect class="hitch" x="42" y="264" width="24" height="8"/>
    <rect class="body-frame" x="125" y="40" width="765" height="292"/>
    <rect class="fill-dark" x="127" y="50" width="761" height="23"/>
    <rect class="fill-light" x="127" y="73" width="761" height="4"/>
    <path class="fill-light" d="M128 165 H855 a12.5 12.5 0 0 1 0 25 H128 Z"/>
    <rect class="fill-dark" x="127" y="210" width="761" height="80"/>
    <rect class="fill-light" x="127" y="292" width="761" height="32"/>
    <rect class="frame-rail" x="127" y="324" width="761" height="8"/>
    <rect class="lamp-amber" x="147" y="42" width="10" height="5"/>
    <rect class="lamp-red" x="845" y="42" width="12" height="5"/>
    <circle class="tire" cx="527" cy="338" r="32"/>
    <circle class="rim" cx="527" cy="338" r="20"/>
    <circle class="tire" cx="642" cy="338" r="32"/>
    <circle class="rim" cx="642" cy="338" r="20"/>
    <circle class="fill-light" cx="538" cy="140" r="10"/>
    <text class="brand-name" x="848" y="151" font-size="29" text-anchor="end">Greenvale Grounds</text>
    <text class="contact contact--dark" x="148" y="186" font-size="21">555.014.2286</text>
    <text class="contact contact--white" x="848" y="280" font-size="21" text-anchor="end">gvgrounds.com</text>
  </g>

  <!-- Rear view -->
  <g class="trailer trailer--rear">
    <rect class="tire" x="958" y="325" width="34" height="38" rx="6"/>
    <rect class="tire" x="1198" y="325" width="34" height="38" rx="6"/>
    <rect class="body-frame" x="950" y="38" width="290" height="300" rx="6"/>
    <rect class="fill-dark" x="973" y="55" width="244" height="18"/>
    <rect class="fill-light" x="973" y="73" width="244" height="3"/>
    <rect class="fill-white" x="973" y="76" width="244" height="131"/>
    <rect class="fill-dark" x="973" y="207" width="244" height="84"/>
    <rect class="fill-light" x="973" y="291" width="244" height="31"/>
    <rect class="lamp-red" x="1030" y="39" width="12" height="4"/>
    <rect class="lamp-red" x="1090" y="39" width="12" height="4"/>
    <rect class="lamp-red" x="1148" y="39" width="12" height="4"/>
    <rect class="lamp-red" x="951" y="178" width="14" height="22" rx="5"/>
    <rect class="lamp-red" x="951" y="206" width="14" height="22" rx="5"/>
    <rect class="lamp-red" x="1225" y="178" width="14" height="22" rx="5"/>
    <rect class="lamp-red" x="1225" y="206" width="14" height="22" rx="5"/>
    <text class="brand-name" x="1095" y="145" font-size="20" text-anchor="middle">Greenvale Grounds</text>
    <text class="contact contact--dark" x="1095" y="188" font-size="21" text-anchor="middle">555.014.2286</text>
    <text class="contact contact--white" x="1095" y="280" font-size="21" text-anchor="middle">gvgrounds.com</text>
  </g>

  <!-- Curb side view -->
  <g class="trailer trailer--curb-side">
    <rect class="ground-shadow" x="55" y="732" width="800" height="6" rx="3"/>
    <rect class="hitch" x="815" y="654" width="110" height="16" rx="6"/>
    <rect class="hitch" x="880" y="612" width="9" height="56"/>
    <rect class="hitch" x="872" y="630" width="24" height="8"/>
    <rect class="body-frame" x="50" y="407" width="767" height="290"/>
    <rect class="frame-rail" x="52" y="409" width="763" height="6"/>
    <path class="fill-light" d="M76 558 H495 a13.5 13.5 0 0 1 0 27 H76 Z"/>
    <rect class="fill-dark" x="52" y="617" width="763" height="53"/>
    <rect class="fill-light" x="52" y="672" width="763" height="20"/>
    <rect class="frame-rail" x="52" y="692" width="763" height="5"/>
    <rect class="lamp-red" x="84" y="409" width="12" height="5"/>
    <rect class="lamp-amber" x="786" y="409" width="10" height="5"/>
    <rect class="door" x="541" y="431" width="159" height="186"/>
    <rect class="door-handle" x="546" y="555" width="9" height="22" rx="2"/>
    <circle class="tire" cx="300" cy="706" r="30"/>
    <circle class="rim" cx="300" cy="706" r="19"/>
    <circle class="tire" cx="415" cy="706" r="30"/>
    <circle class="rim" cx="415" cy="706" r="19"/>
    <circle class="fill-light" cx="94" cy="527" r="13"/>
    <text class="brand-name" x="118" y="540" font-size="35">Greenvale Grounds</text>
    <text class="contact contact--white" x="76" y="653" font-size="19">555.014.2286</text>
    <text class="contact contact--white" x="560" y="653" font-size="19">gvgrounds.com</text>
  </g>

  <text class="sheet-title" x="93" y="848" font-size="40">24 FOOT TRAILER</text>
</svg>
</body>
</html>
```